I need a new business card for my hair salon based in Larkfield, OR called "Lune's Salon". I have been in business at the same location for the past 15 years, and have recently remodeled the place to be a little bit more upscale and modern. Previously, my clientele's were mostly men, but now I would like to attract more female clientele into my business. I would like the design to attract the female's attention with it's modern touch, flowery, freshness with just enough information and not too compact. Simple, clean and professional is the look.
Requirements
Must Have:
- The design should include:
Business name: Lune's Salon
Hairstylist/Owner Name: Lune Okafor
Phone Number: (555) 418-6037
Website: www.lunehairstudio.example
Address: 48390 Harlow Penn Circle
Larkfield, OR 20517
FRONT CARD should include:
- Logo (Business name)
- Slogan (Soft curls, bright days)
BACK CARD should include:
- Logo (Business name)
- Hairstyle name
- Phone number
- Website
- Address
Reason: There were some good submission for this project, but most of the submission were poorly designed, and did not have what I want. There isn't enough designs for me to choose from and not one of it stood out to me. I would like to extend it a bit longer to see if any other designer would step up to the plate, and deliver. Thank you.
Requirements
Must have
- The front side of the business card should only have the business name (Lune's Salon) and slogan, (Soft curls bright days) with a creative design.
The back side of the business card should have all the business information, and creative design that matches with the front, but not identical.
The first letter (V) in (Lune's) should have a flower design connected to it, which blends into the background design.
Nice to have
- Light color scheme.
Should not have
- The front, and back should not have the same design.
Do not include illustrations of a pair of scissors, combs or any objects in the design.
The design should not take the main focus from the business name and business information. It should blend well together... if that's possible.

```html
<!DOCTYPE html>
<html lang="en">
<head>
<meta charset="utf-8">
<title>Lune's Salon – Business Card</title>
<link rel="stylesheet" href="https://fonts.googleapis.com/css2?family=Open+Sans:wght@400;600&family=Crimson+Text:wght@600&display=swap">
<style>
  :root {
    --page: #e9e9ec;
    --card: #ffffff;
    --plum: #4a1d5e;
    --plum-deep: #3f1852;
    --ink: #1b1b1d;
    --text: #2a2a2a;
    --hair-dark: #151515;
    --hair-mid: #6d6d70;
  }
  * { box-sizing: border-box; margin: 0; padding: 0; }
  html, body { width: 1200px; height: 750px; overflow: hidden; }
  body {
    background: var(--page);
    font-family: "Open Sans", sans-serif;
    display: flex;
    align-items: center;
    justify-content: center;
    gap: 30px;
  }
  .card {
    position: relative;
    width: 540px;
    height: 312px;
    background: var(--card);
    border-radius: 22px;
    overflow: hidden;
  }
  .card-art { position: absolute; inset: 0; width: 100%; height: 100%; }

  .brand {
    position: absolute;
    text-align: center;
    color: var(--plum);
  }
  .brand-name {
    font-family: "Open Sans", sans-serif;
    font-weight: 600;
    font-size: 28px;
    letter-spacing: 0.3px;
    line-height: 1.1;
  }
  .brand-slogan {
    font-family: "Crimson Text", serif;
    font-weight: 600;
    font-size: 15px;
    margin-top: 2px;
  }
  .front .brand { left: 26px; top: 196px; width: 196px; }
  .back .brand { right: 40px; top: 86px; width: 190px; }

  .owner { position: absolute; left: 28px; top: 100px; }
  .owner-name { color: var(--plum); font-size: 19px; font-weight: 400; }
  .owner-role { color: var(--text); font-size: 14.5px; margin-top: 2px; }

  .contact {
    position: absolute;
    left: 33px;
    top: 166px;
    list-style: none;
    color: var(--text);
    font-size: 14px;
    line-height: 19.5px;
  }
  .contact li { display: flex; gap: 10px; }
  .contact svg { width: 13px; height: 13px; margin-top: 3px; flex: none; fill: var(--plum); }
</style>
</head>
<body>

  <section class="card front" aria-label="Front of card">
    <svg class="card-art" viewBox="0 0 540 312" aria-hidden="true">
      <polygon points="0,312 0,246 84,312" fill="var(--plum)"/>
    </svg>
    <svg class="card-art" viewBox="0 0 540 312" role="img" aria-label="Illustration of a woman with flowing hair over a dark floral pattern">
      <defs>
        <linearGradient id="hairTone" x1="0" y1="0" x2="1" y2="0.4">
          <stop offset="0" stop-color="var(--hair-dark)"/>
          <stop offset="0.45" stop-color="var(--hair-mid)"/>
          <stop offset="0.75" stop-color="#f4f4f4"/>
          <stop offset="1" stop-color="#ffffff"/>
        </linearGradient>
      </defs>
      <polygon points="0,0 540,0 540,312 388,312 0,60" fill="url(#hairTone)"/>
    </svg>
    <div class="brand">
      <p class="brand-name">Lune's Salon</p>
      <p class="brand-slogan">Soft curls, bright days</p>
    </div>
  </section>

  <section class="card back" aria-label="Back of card">
    <svg class="card-art" viewBox="0 0 540 312" aria-hidden="true">
      <path d="M0,246 C125,281 308,285 540,237 L540,312 L0,312 Z" fill="var(--ink)"/>
      <path d="M0,268 C145,289 318,285 540,252" fill="none" stroke="#ffffff" stroke-width="2.5"/>
      <path d="M0,272 C154,291 328,287 540,258 L540,312 L0,312 Z" fill="var(--plum-deep)"/>
    </svg>

    <div class="owner">
      <p class="owner-name">Lune Okafor</p>
      <p class="owner-role">Hairstylist/Owner</p>
    </div>

    <ul class="contact">
      <li>
        <svg viewBox="0 0 16 16" aria-hidden="true"><path d="M1 5c0-2 3-3 7-3s7 1 7 3v1h-4V5H5v1H1z M3 7h10l1 7H2z M6 9a2 2 0 1 0 4 0a2 2 0 1 0-4 0z" fill-rule="evenodd"/></svg>
        <span>(555) 418-6037</span>
      </li>
      <li>
        <svg viewBox="0 0 16 16" aria-hidden="true"><circle cx="8" cy="8" r="6.3" fill="none" stroke="var(--plum)" stroke-width="1.3"/><ellipse cx="8" cy="8" rx="2.6" ry="6.3" fill="none" stroke="var(--plum)" stroke-width="1.1"/><path d="M1.8 8h12.4" stroke="var(--plum)" stroke-width="1.1"/></svg>
        <span>www.lunehairstudio.example</span>
      </li>
      <li>
        <svg viewBox="0 0 16 16" aria-hidden="true"><path d="M8 1a5 5 0 0 0-5 5c0 4 5 9 5 9s5-5 5-9a5 5 0 0 0-5-5zm0 3a2 2 0 1 1 0 4a2 2 0 0 1 0-4z" fill-rule="evenodd"/></svg>
        <span>48390 Harlow Penn Circle<br>Larkfield, OR 20517</span>
      </li>
    </ul>

    <div class="brand">
      <p class="brand-name">Lune's Salon</p>
      <p class="brand-slogan">Soft curls, bright days</p>
    </div>
  </section>

</body>
</html>
```